Maplecrest geriatric care need flyer design

Flyer design to introduce physician working with maplecrest geriatric care.
the flyer can be simple but need to be catchy.
A sample attached just mainly for reference purpose.
The format must be editable with ms word.

thank you

```html
<!DOCTYPE html>
<html lang="en">
<head>
<meta charset="utf-8">
<title>Maplecrest Geriatric Care – Introducing Dr. Abcxyz Pqr</title>
<link href="https://fonts.googleapis.com/css2?family=Jost:wght@400;500&display=swap" rel="stylesheet">
<style>
  :root{
    --navy:#232e6b;
    --red:#d42027;
    --ink:#2b3270;
    --grey-light:#efefef;
    --grey-dark:#cfcfcf;
    --white:#ffffff;
  }
  *{box-sizing:border-box;margin:0;padding:0}
  html,body{width:848px;height:1200px;overflow:hidden;background:var(--white)}
  body{font-family:"Jost",Arial,sans-serif;color:var(--ink)}
  .flyer{position:relative;width:848px;height:1200px;overflow:hidden;background:var(--white)}
  .header-wash{position:absolute;left:0;top:0;width:848px;height:250px}
  .brand{position:absolute;right:22px;top:38px}
  .brand-name{display:flex;align-items:center;gap:12px;font-size:40px;font-weight:500;color:var(--navy);line-height:1}
  .brand-dot{width:30px;height:30px;border-radius:50%;background:var(--red);flex:none}
  .intro-label{position:absolute;left:48px;top:168px;font-size:23px;color:var(--navy);letter-spacing:.3px}
  .name-band{position:absolute;left:0;top:269px;width:772px;height:94px;background:var(--navy);border-top-right-radius:20px}
  .title-band{position:absolute;left:0;top:362px;width:772px;height:55px;background:var(--red);border-bottom-right-radius:20px}
  .portrait{position:absolute;left:46px;top:220px;width:185px;height:182px;border:5px solid var(--white);
    background:linear-gradient(160deg,#eef2f4 0%,#d9dfe3 45%,#b9c1c8 100%);box-shadow:0 2px 6px rgba(0,0,0,.35)}
  .doctor-name{position:absolute;left:254px;top:282px;font-size:23px;color:var(--white)}
  .doctor-creds{position:absolute;left:254px;top:320px;font-size:17.5px;color:var(--white)}
  .doctor-role{position:absolute;left:254px;top:371px;font-size:24px;color:var(--white);letter-spacing:.2px}
  .bio{position:absolute;left:131px;top:447px;width:611px;font-size:16.5px;line-height:21px;color:var(--ink)}
  .bio p{text-align:justify;margin-bottom:6px}
  .bio h2{font-weight:400;color:var(--red);font-size:20.5px;line-height:24px;margin-top:10px;margin-bottom:4px}
  .bio h3{font-weight:400;color:var(--red);font-size:19px;line-height:23px;margin-top:10px}
  .interests{list-style:none;margin-bottom:6px}
  .interests li{line-height:23.5px}
  .interests li::before{content:"\25CF";font-size:12px;margin-right:6px;vertical-align:1px}
  .bio .left{text-align:left}
  .bio strong{font-weight:500}
  .footer-band{position:absolute;left:0;bottom:0;width:848px;height:46px;background:var(--navy)}
  .contact-card{position:absolute;left:124px;top:962px;width:501px;height:208px;background:var(--white);
    border:2px solid var(--red);border-top-width:8px;border-radius:18px;padding:16px 20px 0 22px}
  .contact-card h2{font-weight:400;font-size:24px;color:var(--navy);margin-bottom:6px}
  .contact-card p{font-size:16.5px;line-height:20px;color:var(--ink)}
  .contact-card .accent{color:var(--red)}
  .contact-card .practice{font-size:20px;color:var(--red);margin-top:6px;line-height:23px}
  .contact-card .numbers{font-size:20px;color:var(--red);margin-top:8px}
</style>
</head>
<body>
<main class="flyer">
  <svg class="header-wash" viewBox="0 0 848 250" aria-hidden="true">
    <defs>
      <linearGradient id="wash" x1="0" y1="0" x2="1" y2="1">
        <stop offset="0" stop-color="var(--grey-light)"/>
        <stop offset="1" stop-color="var(--grey-dark)"/>
      </linearGradient>
    </defs>
    <path d="M0,0 H848 V200 C700,185 560,175 420,150 C280,125 140,95 0,80 Z" fill="url(#wash)"/>
  </svg>

  <div class="brand">
    <div class="brand-name"><span class="brand-dot"></span>Maplecrest Geriatric Care</div>
  </div>

  <div class="intro-label">INTRODUCING</div>

  <div class="name-band"></div>
  <div class="title-band"></div>
  <div class="portrait" role="img" aria-label="Portrait photograph of the consultant geriatrician"></div>
  <div class="doctor-name">Dr. Abcxyz Pqr</div>
  <div class="doctor-creds">MBBS (Kingsford), FRACP, Clin Dip Pall med.</div>
  <div class="doctor-role">CONSULTANT GERIATRICIAN &amp; PHYSICIAN</div>

  <section class="bio">
    <p class="left">We are very pleased to introduce you to Dr. Abcxyz (MBBS, FRACP)<br>Consultant Geriatrician and Physician who has commenced consulting at Maplecrest Geriatric Care and is available to see patients who are 65 years and over.</p>
    <p>Dr. abcxyz completed his specialist training with Southern Bay Health in 2012 and then undertook 60 months of diploma training in palliative care medicine prior to commencing as a consultant Geriatrician.</p>
    <h2>He has an interest in all geriatric related problems, with special interest in:</h2>
    <ul class="interests">
      <li>Comprehensive geriatric assessment (Over 65 Years)</li>
      <li>Memory assessment</li>
      <li>Fall and balance assessment</li>
      <li>Polypharmacy</li>
    </ul>
    <p class="left">He is also available to visit residential care facilities, should you require any advice.</p>
    <h3>Other languages spoken:</h3>
    <p class="left">Mandarin, Cantonese &amp; Malay</p>
    <p class="left">Daniel can be contacted on <strong>0400 555 218</strong> for patient advice.</p>
    <p class="left">Alternatively, you can fax your referral especially for residents in residential care facilities to <strong>(03) 5550 1947</strong>.</p>
  </section>

  <div class="footer-band"></div>

  <section class="contact-card">
    <h2>Contact Details</h2>
    <p>To arrange an appointment for your patient with <span class="accent">Dr. abcxyz,</span><br>Please Contact:</p>
    <p class="practice">Maplecrest Geriatric Care</p>
    <p>128-134 Linden Avenue<br>Ashford Park, Vic 3990</p>
    <p class="numbers">Phone: (00) 0000 0000 &nbsp;|&nbsp; Fax: (00) 0000 0001</p>
  </section>
</main>
</body>
</html>
```